Business card design - landscaping industry

Hello! We are very creative when it comes to landscape design but when it comes to designing business cards - not so much. We could use some help to come up with a design which is professional but fun. We are based in Grand Rapids, MI and work with high end properties for new landscape design and install. We are looking to have a template made for business card for a couple of us on staff.

You can get the flavor of our color scheme from our attached logo. We probably would want to highlight the green but also include some of the blue maybe.

Target Market(s)

We work with residential homeowners here in West Michigan. Very nice people by and large.

Industry/Entity Type

Landscaping

Contact Information for Business Card

The card should be standard size with round edges maybe?

Font styles to use
Serif
Sans Serif
Decorative

Requirements
Must have
• Must haves:
• 1. Address: 4817 Birchwell Meadow Lane SE, Grand Rapids, Michigan 49582
• 2. Phone: 616.555.0187
• 3. Email: company@larkhollowyard.com
• 4. URL: www.larkhollowyard.com
• 5. Names/Titles: (1) Dennis Harlow, President (2) Tomas Belvin, Director of Field Services
Nice to have
• On the back side of the card, we are thinking it would make sense to have a short listing of services offered...
• Landscape design & installation, Professional lawn maintenance, Spring & fall leaf cleanup, Irrigation system installation & maintenance, Snowplowing, Fertilizer & weed control, Tree maintenance and removal, Landscape bed maintenance
Should not have
• Our hope is that the design won't be too ostentatious. We are looking for professional and attractive.

```html
<!DOCTYPE html>
<html lang="en">
<head>
<meta charset="utf-8">
<title>Lark Hollow Landscaping – Business Card</title>
<link rel="stylesheet" href="https://fonts.googleapis.com/css2?family=Cinzel:wght@400;500&family=Arimo:wght@400&display=swap">
<style>
  :root {
    --page-bg: #e8e8e8;
    --card-dark: #363f42;
    --card-light: #f7f7f7;
    --brand-blue: #2a8ccf;
    --brand-green: #3fa14a;
    --ink-dark: #2f3538;
    --ink-light: #d2d7d9;
    --logo-light: #e4e8ea;
    --logo-dark: #3a4448;
  }
  * { margin: 0; padding: 0; box-sizing: border-box; }
  html, body { width: 1200px; height: 576px; overflow: hidden; }
  body {
    background: var(--page-bg);
    position: relative;
    font-family: "Arimo", Arial, sans-serif;
  }
  .card {
    position: absolute;
    border-radius: 13px;
    overflow: hidden;
  }
  .card--back {
    left: 82px; top: 139px; width: 484px; height: 291px;
    background: var(--card-dark);
  }
  .card--front {
    left: 602px; top: 138px; width: 481px; height: 292px;
    background: var(--card-light);
  }
  .wordmark {
    position: absolute;
    font-family: "Cinzel", Georgia, serif;
    font-weight: 400;
    text-align: center;
    line-height: 1;
  }
  .card--back .wordmark {
    left: 0; right: 0; top: 90px;
    color: var(--logo-light);
  }
  .wordmark__name { display: block; font-size: 34px; letter-spacing: 5px; }
  .wordmark__tag { display: block; font-size: 11px; letter-spacing: 9px; margin-top: 10px; }
  .services {
    position: absolute; left: 0; right: 0; top: 206px;
    text-align: center;
    color: var(--ink-light);
    font-size: 10.5px;
    line-height: 15px;
  }
  .services .sep-g { color: var(--brand-green); }
  .services .sep-b { color: var(--brand-blue); }

  .staff { position: absolute; left: 23px; top: 30px; }
  .staff__name {
    font-family: "Cinzel", Georgia, serif;
    color: var(--brand-blue);
    font-size: 17.5px;
    letter-spacing: 0.5px;
    line-height: 1;
  }
  .staff__title { color: var(--ink-dark); font-size: 10px; margin-top: 2px; margin-bottom: 10px; }
  .address {
    position: absolute; left: 23px; top: 174px;
    color: var(--ink-dark); font-size: 11.5px; line-height: 16px;
  }
  .contacts { position: absolute; left: 23px; top: 212px; list-style: none; }
  .contacts li {
    display: flex; align-items: center;
    color: var(--ink-dark); font-size: 11.5px; height: 15px;
  }
  .contacts svg { width: 10px; height: 10px; margin-left: 1px; margin-right: 12px; }
  .card--front .wordmark {
    left: 234px; width: 230px; top: 222px;
    color: var(--logo-dark);
  }
  .card--front .wordmark__name { font-size: 22px; letter-spacing: 3px; }
  .card--front .wordmark__tag { font-size: 7.5px; letter-spacing: 6px; margin-top: 6px; }
  .card__band { position: absolute; left: 0; bottom: 0; width: 481px; height: 8px; }
</style>
</head>
<body>
  <section class="card card--back" aria-label="Card back">
    <div class="wordmark">
      <span class="wordmark__name">LARK HOLLOW</span>
      <span class="wordmark__tag">LANDSCAPING</span>
    </div>
    <p class="services">
      Landscape Design &amp; Installation <span class="sep-b">|</span> Professional Lawn Maintenance<br>
      Spring &amp; Fall Leaf Cleanup <span class="sep-g">|</span> Irrigation System Installation &amp; Maintenance<br>
      Snowplowing <span class="sep-b">|</span> Fertilizer &amp; Weed Control<br>
      Tree Maintenance &amp; Removal <span class="sep-g">|</span> Landscape Bed Maintenance
    </p>
  </section>

  <section class="card card--front" aria-label="Card front">
    <div class="staff">
      <p class="staff__name">DENNIS HARLOW</p>
      <p class="staff__title">President</p>
      <p class="staff__name">TOMAS BELVIN</p>
      <p class="staff__title">Director of Field Services</p>
    </div>
    <p class="address">4817 Birchwell Meadow Lane SE,<br>Grand Rapids, Michigan 49582</p>
    <ul class="contacts">
      <li>
        <svg viewBox="0 0 10 10" aria-hidden="true"><path d="M1 3 Q1 1 5 1 Q9 1 9 3 L7 4 L6 3 L4 3 L3 4 Z M3 5 L7 5 L8.5 9 L1.5 9 Z" fill="var(--brand-blue)"/></svg>
        616.555.0187
      </li>
      <li>
        <svg viewBox="0 0 10 10" aria-hidden="true"><rect x="0.5" y="2" width="9" height="6.5" fill="var(--brand-blue)"/><path d="M0.8 2.3 L5 5.8 L9.2 2.3" stroke="#fff" stroke-width="0.9" fill="none"/></svg>
        company@larkhollowyard.com
      </li>
      <li>
        <svg viewBox="0 0 10 10" aria-hidden="true"><circle cx="5" cy="5" r="4.3" fill="var(--brand-blue)"/><path d="M0.7 5 H9.3 M5 0.7 V9.3 M5 0.7 Q2 5 5 9.3 M5 0.7 Q8 5 5 9.3" stroke="#fff" stroke-width="0.6" fill="none"/></svg>
        www.larkhollowyard.com
      </li>
    </ul>
    <div class="wordmark">
      <span class="wordmark__name">LARK HOLLOW</span>
      <span class="wordmark__tag">LANDSCAPING</span>
    </div>
    <svg class="card__band" viewBox="0 0 481 8" preserveAspectRatio="none" aria-hidden="true">
      <rect x="0" y="0" width="481" height="8" fill="var(--brand-blue)"/>
      <polygon points="0,0 155,0 163,8 0,8" fill="var(--brand-green)"/>
    </svg>
  </section>
</body>
</html>
```